Double Sided Flyer for 3D printing services company

We need a nice balanced flyer for our corporate handout. The attached is for concept only and not the final design. We think the attached examples have elements that balance nicely but the graphics are not good. We are attaching the logo from the corporate office for our new logo. We will add the company information after the final design is selected for web address, phone, mailing etc. Please leave room for that information in the design. Please ask any questions prior to submission. Our main focus is printing RUBBER 3D Parts and not plastic parts. The images selected should be focused on that. We also need to ensure the images are approved for use in a corporate flyer for content.

```html
<!DOCTYPE html>
<html lang="en">
<head>
<meta charset="utf-8">
<title>Veranto Flyer – Front and Back</title>
<link rel="stylesheet" href="https://fonts.googleapis.com/css2?family=Poppins:wght@400;500;600;700;800;900&display=swap">
<style>
  :root {
    --backdrop: #e9e6e2;
    --ink-dark: #3a3a3a;
    --panel-dark: #454545;
    --panel-deep: #2f2f2f;
    --orange: #f26a1b;
    --orange-deep: #e2531a;
    --white: #ffffff;
    --muted: #d4d4d4;
    --paper: #f4f4f3;
  }
  * { margin: 0; padding: 0; box-sizing: border-box; }
  html, body { width: 1200px; height: 900px; overflow: hidden; }
  body {
    background: var(--backdrop);
    font-family: "Poppins", sans-serif;
    position: relative;
  }
  .flyer {
    position: absolute;
    top: 100px;
    width: 500px;
    height: 700px;
    overflow: hidden;
  }
  .flyer--front { left: 70px; background: var(--paper); }
  .flyer--back {
    left: 630px;
    background: linear-gradient(160deg, #4a4a4a 0%, #3d3d3d 55%, #333 100%);
    color: var(--white);
  }

  /* ---------- Front ---------- */
  .brand {
    position: absolute; top: 28px; left: 0; width: 100%;
    display: flex; flex-direction: column; align-items: center;
  }
  .brand__row { display: flex; align-items: center; gap: 10px; }
  .brand__dot { width: 30px; height: 30px; border-radius: 50%; background: var(--orange); }
  .brand__name { font-weight: 800; font-size: 36px; color: var(--ink-dark); line-height: 1; letter-spacing: 0.5px; }
  .brand__tagline { font-size: 11px; letter-spacing: 2px; color: var(--ink-dark); margin-top: 4px; margin-left: 40px; font-weight: 500; }

  .product-hero {
    position: absolute; top: 95px; left: 20px; width: 460px; height: 270px;
    background: radial-gradient(ellipse at 55% 50%, #e4e1dd 0%, #efeeec 60%, transparent 75%);
  }
  .front-shape { position: absolute; left: 0; top: 0; width: 500px; height: 700px; }

  .photo-circle {
    position: absolute; border-radius: 50%; border: 5px solid var(--white);
  }
  .photo-circle--one { left: 44px; top: 330px; width: 170px; height: 170px;
    background: radial-gradient(circle at 45% 45%, #f0a928 0%, #3a4048 55%, #22262b 100%); }
  .photo-circle--two { left: 243px; top: 386px; width: 132px; height: 132px;
    background: radial-gradient(circle at 50% 50%, #5a5a5a 0%, #1f1f1f 70%, #ececec 100%); }
  .photo-circle--three { left: 390px; top: 360px; width: 132px; height: 132px;
    background: radial-gradient(circle at 40% 65%, #2f6fd8 0%, #1c2f55 55%, #6d7d94 100%); }

  .front-title {
    position: absolute; left: 30px; top: 532px; color: var(--white);
    font-weight: 800; text-transform: uppercase;
  }
  .front-title__main { font-size: 48px; line-height: 1; letter-spacing: 0.5px; }
  .front-title__sub { font-size: 26px; line-height: 1.08; margin-top: 4px; }

  .front-points {
    position: absolute; left: 298px; top: 540px; width: 190px; list-style: none;
    color: var(--white); font-weight: 700; font-size: 12.5px; line-height: 1.2;
  }
  .front-points li { position: relative; padding-left: 13px; margin-bottom: 7px; }
  .front-points li::before {
    content: ""; position: absolute; left: 0; top: 5px; width: 5px; height: 5px;
    border-radius: 50%; background: var(--orange);
  }

  .contact-bar {
    position: absolute; left: 0; bottom: 0; width: 100%; height: 36px;
    display: flex; align-items: center; gap: 16px; padding: 4px 0 0 32px;
    color: var(--white); font-weight: 700; font-size: 11px;
  }
  .contact-bar span { display: flex; align-items: center; gap: 4px; }
  .contact-bar svg { width: 11px; height: 11px; fill: var(--white); }

  /* ---------- Back ---------- */
  .parts-backdrop {
    position: absolute; left: 0; top: 370px; width: 500px; height: 180px;
    background: radial-gradient(ellipse at 55% 50%, rgba(30,30,30,0.55) 0%, rgba(40,40,40,0.25) 50%, transparent 75%);
  }
  .back-content { position: absolute; left: 56px; top: 55px; right: 40px; }
  .eyebrow { font-weight: 700; font-size: 19px; letter-spacing: 0.3px; }
  .headline { font-weight: 800; font-size: 43px; line-height: 1.05; margin-top: 6px; text-transform: uppercase; }
  .headline__accent { color: var(--orange); display: block; }
  .subhead { font-weight: 700; font-size: 26px; margin-top: 6px; line-height: 1.2; }
  .intro { font-size: 15px; color: var(--muted); margin-top: 12px; line-height: 1.45; }
  .steps { list-style: none; margin-top: 8px; font-size: 13px; color: var(--muted); }
  .steps li { position: relative; padding-left: 14px; margin-bottom: 3px; }
  .steps li::before {
    content: ""; position: absolute; left: 0; top: 7px; width: 5px; height: 5px;
    border-radius: 50%; background: var(--orange);
  }
  .benefits-title { font-weight: 800; font-size: 32px; margin-top: 14px; }

  .benefit { display: flex; align-items: flex-start; gap: 12px; margin-top: 16px; }
  .benefit:first-of-type { margin-top: 14px; }
  .benefit__icon {
    flex: none; width: 54px; height: 54px; border-radius: 50%;
    background: linear-gradient(150deg, var(--orange) 0%, var(--orange-deep) 100%);
    display: flex; align-items: center; justify-content: center; margin-left: -4px;
  }
  .benefit__icon svg { width: 30px; height: 30px; fill: none; stroke: var(--white); stroke-width: 2; stroke-linecap: round; stroke-linejoin: round; }
  .benefit__title { font-weight: 700; font-size: 12.5px; text-transform: uppercase; margin-top: 2px; }
  .benefit__text { font-size: 11px; color: var(--muted); line-height: 1.45; margin-top: 2px; }
</style>
</head>
<body>

<section class="flyer flyer--front" aria-label="Flyer front">
  <header class="brand">
    <div class="brand__row">
      <span class="brand__dot"></span>
      <span class="brand__name">VERANTO</span>
    </div>
    <div class="brand__tagline">SEALS·GASKETS·HOSES</div>
  </header>

  <div class="product-hero" role="img" aria-label="Assortment of coloured rubber seals, O-rings and gaskets"></div>

  <svg class="front-shape" viewBox="0 0 500 700" aria-hidden="true">
    <defs>
      <linearGradient id="darkPanel" x1="0" y1="0" x2="0" y2="1">
        <stop offset="0" stop-color="#3b3b3b"/>
        <stop offset="1" stop-color="#555555"/>
      </linearGradient>
    </defs>
    <path d="M0 350 C 40 360, 60 430, 160 455 C 280 480, 380 440, 500 360 L500 700 L0 700 Z" fill="url(#darkPanel)"/>
    <path d="M0 668 C 150 640, 330 640, 500 652 L500 700 L0 700 Z" fill="var(--orange)"/>
  </svg>

  <div class="photo-circle photo-circle--one" role="img" aria-label="3D printed rubber parts in yellow and blue"></div>
  <div class="photo-circle photo-circle--two" role="img" aria-label="Black rubber fittings"></div>
  <div class="photo-circle photo-circle--three" role="img" aria-label="Blue part being 3D printed"></div>

  <h1 class="front-title">
    <div class="front-title__main">VERANTO</div>
    <div class="front-title__sub">Seals Gaskets<br>Hoses</div>
  </h1>

  <ul class="front-points">
    <li>Reduce Time to Market From Weeks to Hours</li>
    <li>Elimminate Costly Design Errors</li>
    <li>Faster Time to Market</li>
    <li>Reduced R and D Budgets</li>
  </ul>

  <footer class="contact-bar">
    <span><svg viewBox="0 0 12 12"><circle cx="6" cy="6" r="5.5"/></svg>www.veranto-parts.com</span>
    <span><svg viewBox="0 0 12 12"><path d="M2.5 0.8l2 2.2-1 1.3c.7 1.5 1.9 2.7 3.4 3.4l1.3-1 2.2 2-1 2C5.5 10.5 1.5 6.5 .7 1.8z"/></svg>+1 555 010 4477</span>
    <span><svg viewBox="0 0 12 12"><path d="M6 0a4 4 0 0 1 4 4c0 3-4 8-4 8S2 7 2 4a4 4 0 0 1 4-4zm0 2.4a1.6 1.6 0 1 0 0 3.2 1.6 1.6 0 0 0 0-3.2z"/></svg>Some goes address here</span>
  </footer>
</section>

<section class="flyer flyer--back" aria-label="Flyer back">
  <div class="parts-backdrop" role="img" aria-label="Faint scattered dark rubber O-rings and gaskets"></div>
  <div class="back-content">
    <p class="eyebrow">QUICK PROTOTYPING</p>
    <h2 class="headline">Redefine your industry with <span class="headline__accent">3D Printing</span></h2>
    <p class="subhead">Gaskets and Rubber Parts</p>
    <p class="intro">Need quality parts? Let us print your custom one-of our production pieces.</p>
    <ul class="steps">
      <li>Send us your Rubber part design file</li>
      <li>Receive your Estimate within 24 hours</li>
      <li>Receive your prototype sample within 10 days</li>
    </ul>
    <h3 class="benefits-title">BENEFITS</h3>

    <div class="benefit">
      <div class="benefit__icon"><svg viewBox="0 0 30 30"><path d="M16 5a10 10 0 1 1-2 19.8"/><path d="M16 15l4-4"/><path d="M4 11h7M3 15h8M4 19h7"/></svg></div>
      <div>
        <p class="benefit__title">Speed Time to Market</p>
        <p class="benefit__text">Compress design cycles by 3D printing multiple<br>prototypes on demand, right in your office.</p>
      </div>
    </div>
    <div class="benefit">
      <div class="benefit__icon"><svg viewBox="0 0 30 30"><path d="M6 12a10 10 0 0 1 17-4l2-2v6h-6"/><path d="M24 18a10 10 0 0 1-17 4l-2 2v-6h6"/><path d="M17.5 11.5c-.5-1-1.5-1.5-2.5-1.5-1.6 0-2.5.9-2.5 2 0 2.6 5 1.5 5 4.2 0 1.1-1 2-2.5 2-1.2 0-2.2-.6-2.6-1.6M15 8.5v13"/></svg></div>
      <div>
        <p class="benefit__title">Reduce Development Costs</p>
        <p class="benefit__text">Cut traditional prototyping and tooling costs.Identify design<br>error earlier and reduce travel to production facilities.</p>
      </div>
    </div>
    <div class="benefit">
      <div class="benefit__icon"><svg viewBox="0 0 30 30"><circle cx="15" cy="12" r="7"/><path d="M15 8.5l1.1 2.2 2.4.3-1.7 1.7.4 2.4-2.2-1.1-2.2 1.1.4-2.4-1.7-1.7 2.4-.3z"/><path d="M11 18l-2 8 3-1.5 2 2.5 1-7M19 18l2 8-3-1.5-2 2.5-1-7"/></svg></div>
      <div>
        <p class="benefit__title">Win Business</p>
        <p class="benefit__text">Bring realestic 3D models to prospective accounts, sponsors<br>and focus groups.</p>
      </div>
    </div>
  </div>
</section>

</body>
</html>
```